Ward Compass Business Card Design*

We need a business card design for our company Ward Compass. Our company is specialized in providing online consulting services regarding medical institutions, hospitals and doctors. We work with patients worldwide looking to choose between healthcare providers. We have a website you may use as a reference, where we list doctors and clinics worldwide. So we target Medical providers as well as patients worldwide.
Target Market(s)
Medical Providers and patients around the world
Industry/Entity Type
Medical
Contact Information for Business Card
Salma Derkaoui
CEO
+90 612 348 2071
info@wardcompass-example.com
www.wardcompass-example.com
14 Annakhil 3 H.R.B. Rabat, Morocco
Requirements
Must have
- Company logo/name on one full side, personal info and smaller logo and company name on the other side.
Nice to have
- Smart and elegant design

```html
<!DOCTYPE html>
<html lang="en">
<head>
<meta charset="utf-8">
<title>Ward Compass Business Card</title>
<link rel="stylesheet" href="https://fonts.googleapis.com/css2?family=Montserrat:wght@500&family=Arimo:wght@400;700&display=swap">
<style>
  :root {
    --navy: #1d2f66;
    --white: #ffffff;
    --ink-grey: #4a4d55;
    --page: #d9d9db;
    --line: rgba(255,255,255,0.85);
  }
  * { margin: 0; padding: 0; box-sizing: border-box; }
  html, body { width: 1200px; height: 1200px; overflow: hidden; }
  body {
    background: var(--page);
    font-family: "Arimo", Arial, sans-serif;
    position: relative;
  }
  .card {
    position: absolute;
    left: 250px;
    width: 700px;
    height: 400px;
    box-shadow: 0 6px 18px rgba(0,0,0,0.18);
  }
  .card-front { top: 160px; background: var(--white); }
  .card-back { top: 640px; background: var(--navy); color: var(--white); }

  .front-brand {
    position: absolute;
    left: 0; right: 0; top: 0; bottom: 0;
    display: flex;
    align-items: center;
    justify-content: center;
    gap: 22px;
  }
  .brand-dot {
    width: 70px; height: 70px;
    border-radius: 50%;
    background: var(--navy);
  }
  .brand-name {
    font-family: "Montserrat", Arial, sans-serif;
    font-weight: 500;
    font-size: 50px;
    letter-spacing: 3px;
    text-transform: uppercase;
    color: var(--navy);
  }

  .back-mark {
    position: absolute;
    left: 220px; top: 50px;
    width: 260px;
    display: flex;
    flex-direction: column;
    align-items: center;
    gap: 14px;
  }
  .back-mark .brand-dot { width: 96px; height: 96px; background: var(--white); }
  .back-mark .brand-name { color: var(--white); font-size: 22px; letter-spacing: 2px; }

  .divider {
    position: absolute;
    left: 40px; right: 40px; top: 232px;
    height: 1.5px;
    background: var(--line);
  }
  .person {
    position: absolute;
    left: 40px; top: 250px;
  }
  .person-name { font-weight: 700; font-size: 24px; }
  .person-role { font-size: 17px; margin-top: 4px; }
  .person-rule {
    width: 200px; height: 1.5px;
    background: var(--line);
    margin: 8px 0 10px;
  }
  .contact-list { list-style: none; }
  .contact-list li {
    display: flex;
    align-items: center;
    gap: 12px;
    font-size: 17px;
    line-height: 26px;
  }
  .contact-list svg { width: 13px; height: 13px; flex: none; }

  .address {
    position: absolute;
    right: 40px; top: 250px;
    font-size: 17px;
    line-height: 24px;
    text-align: left;
  }
</style>
</head>
<body>
  <section class="card card-front">
    <div class="front-brand">
      <span class="brand-dot"></span>
      <span class="brand-name">Ward Compass</span>
    </div>
  </section>

  <section class="card card-back">
    <div class="back-mark">
      <span class="brand-dot"></span>
      <span class="brand-name">Ward Compass</span>
    </div>
    <div class="divider"></div>

    <div class="person">
      <p class="person-name">Salma Derkaoui</p>
      <p class="person-role">CEO</p>
      <div class="person-rule"></div>
      <ul class="contact-list">
        <li>
          <svg viewBox="0 0 16 16" aria-hidden="true"><path fill="#fff" d="M3.5 1.5l2.5 0 1 3.5-1.6 1.2a9 9 0 0 0 4.4 4.4L11 9l3.5 1v2.5c0 1-1 2-2 2A11 11 0 0 1 1.5 3.5c0-1 1-2 2-2z"/></svg>
          +90 612 348 2071
        </li>
        <li>
          <svg viewBox="0 0 16 16" aria-hidden="true"><rect x="1" y="3" width="14" height="10" fill="#fff"/><path d="M1 3l7 6 7-6" fill="none" stroke="#1d2f66" stroke-width="1.4"/></svg>
          info@wardcompass-example.com
        </li>
        <li>
          <svg viewBox="0 0 16 16" aria-hidden="true"><g fill="none" stroke="#fff" stroke-width="1.4"><circle cx="8" cy="8" r="6.5"/><ellipse cx="8" cy="8" rx="2.8" ry="6.5"/><path d="M1.5 8h13"/></g></svg>
          info@wardcompass-example.com
        </li>
      </ul>
    </div>

    <address class="address" style="font-style: normal;">
      14 Annakhil 3 H.R.B.<br>
      Rabat, Morocco
    </address>
  </section>
</body>
</html>
```